Travel Company is looking for a STAND OUT Business Card

I need a unique Business Card that will truly stand out. Nothing too busy. Simple is good, right? Not looking for a standard design either. No cookie cutter layout. We are a Travel Company that works more with Companies than Travelers. I had an idea to focus and emphasis on the 2 logo a bit more. This is not necessary, however thought it would look interesting. I am just looking for something interesting and a bit different. Does't have to completely off the wall crazy, just not your run of the mill business card.

Target Market(s)

Hoteliers, Resort Management, Call Centers, Executives, Travelers, Families, Businesses

Industry/Entity Type

Hospitality

Contact Information for Business Card

President/CEO - Marcus T Bellamy (title not necessary if design doesn't allow for it)
contact - (407) 555-0186
email - mbellamy@wayfarenow.example
address - 4812 Quillmore Ave #164
Orlando, FL 32804
website - www.wayfarenow.example

Font styles to use
Serif
Other font styles liked:
• Avenir Next LT Pro BOLD

Requirements
Must have
• simple look and design. Unique design
Nice to have
• I attached the 2 logo separate from the main logo. This can be used separately from the Main Logo, together with the main logo or as main logo. I included the logo font. Use it or not, designers choice.
Should not have
• cookie cutter design. Little use of red other than the logo

```html
<!DOCTYPE html>
<html lang="en">
<head>
<meta charset="utf-8">
<title>Wayfarenow Business Card</title>
<link href="https://fonts.googleapis.com/css2?family=Montserrat:wght@700;800&family=Fira+Sans+Condensed:wght@400;500&display=swap" rel="stylesheet">
<style>
  :root {
    --red: #fc0000;
    --black: #000000;
    --white: #ffffff;
    --ink: #111111;
    --backdrop: #f2f3f3;
    --card-w: 900px;
    --card-h: 550px;
  }
  * { margin: 0; padding: 0; box-sizing: border-box; }
  html, body { width: 1120px; height: 1200px; overflow: hidden; background: var(--backdrop); }
  .sheet {
    width: 1120px; height: 1200px;
    display: flex; flex-direction: column; align-items: center; justify-content: center; gap: 40px;
  }
  .card {
    position: relative; width: var(--card-w); height: var(--card-h);
    overflow: hidden; box-shadow: 0 2px 10px rgba(0,0,0,.12);
  }
  .card--front { background: var(--white); border: 1px solid #9a9a9a; }
  .card--back { background: var(--red); }
  .card__split { position: absolute; inset: 0; width: 100%; height: 100%; }

  .holder { position: absolute; left: 55px; top: 62px; }
  .holder__name {
    font-family: "Montserrat", sans-serif; font-weight: 800; font-size: 44px;
    color: var(--red); line-height: 1;
  }
  .holder__title {
    font-family: "Fira Sans Condensed", sans-serif; font-weight: 400; font-size: 32px;
    color: var(--ink); margin-top: 10px;
  }

  .wordmark {
    position: absolute; display: flex; align-items: center; gap: 14px;
    font-family: "Montserrat", sans-serif; font-weight: 800; white-space: nowrap;
    transform-origin: center; transform: rotate(-21deg);
  }
  .wordmark__dot { border-radius: 50%; flex: none; }
  .card--front .wordmark { left: 95px; top: 260px; font-size: 46px; color: var(--black); }
  .card--front .wordmark__dot { width: 52px; height: 52px; background: var(--red); }
  .card--back .wordmark { left: 95px; top: 250px; font-size: 50px; color: var(--white); }
  .card--back .wordmark__dot { width: 56px; height: 56px; background: var(--white); }

  .address {
    position: absolute; right: 40px; top: 270px; text-align: right;
    font-family: "Fira Sans Condensed", sans-serif; font-weight: 400; font-size: 35px;
    line-height: 1.22; color: var(--ink);
  }
  .phone {
    position: absolute; left: 258px; top: 440px;
    font-family: "Fira Sans Condensed", sans-serif; font-weight: 500; font-size: 62px;
    color: var(--ink); letter-spacing: .5px;
  }
</style>
</head>
<body>
<main class="sheet">
  <section class="card card--front" aria-label="Card front">
    <div class="holder">
      <p class="holder__name">Marcus T Bellamy</p>
      <p class="holder__title">President/CEO</p>
    </div>
    <div class="wordmark"><span class="wordmark__dot"></span>www.wayfarenow.example</div>
    <address class="address">
      4812 Quillmore<br>Ave #164<br>Orlando<br>FL 32804
    </address>
    <p class="phone">(407) 555-0186</p>
  </section>

  <section class="card card--back" aria-label="Card back">
    <svg class="card__split" viewBox="0 0 900 550" preserveAspectRatio="none" aria-hidden="true">
      <polygon points="0,0 862,0 20,550 0,550" fill="var(--black)"/>
    </svg>
    <div class="wordmark"><span class="wordmark__dot"></span>www.wayfarenow.example</div>
  </section>
</main>
</body>
</html>
```